Buch-/eBook-Cover für Sachbuch gesucht
Zielgruppe
We're selfpublishing nonfiction books. Interested are adults - mostly man (age range: 25-50) - who want to learn more about leadership at their workplaces.
Aufgabenstellung
The design should be clean and simple, title easy to read, good color contrast (the cover has to stand out from an white background).

```html
<!DOCTYPE html>
<html lang="en">
<head>
<meta charset="utf-8">
<title>Leadership – Book Cover</title>
<link rel="stylesheet" href="https://fonts.googleapis.com/css2?family=Barlow+Condensed:wght@500;600;700&display=swap">
<style>
  :root {
    --paper: #ece9e1;
    --navy: #233a63;
    --navy-soft: #2b4470;
    --teal: #5ec2d1;
    --red: #d7323d;
  }
  * { margin: 0; padding: 0; box-sizing: border-box; }
  html, body {
    width: 848px;
    height: 1200px;
    overflow: hidden;
    background: var(--paper);
  }
  .cover {
    position: relative;
    width: 848px;
    height: 1200px;
    background: var(--paper);
    font-family: "Barlow Condensed", "Arial Narrow", sans-serif;
  }
  .cover__art {
    position: absolute;
    inset: 0;
    width: 848px;
    height: 1200px;
  }
  .cover__shadow { fill: var(--navy); }
  .title { font-family: "Barlow Condensed", "Arial Narrow", sans-serif; font-weight: 600; }
  .title__top { fill: var(--teal); }
  .title__bottom { fill: var(--navy); }
  .subtitle {
    position: absolute;
    left: 384px;
    top: 616px;
    color: var(--red);
    font-weight: 600;
    font-size: 40px;
    line-height: 40px;
    letter-spacing: -0.2px;
  }
  .walkers {
    position: absolute;
    left: 100px;
    top: 740px;
    width: 312px;
    height: 285px;
    background: radial-gradient(ellipse at center, var(--navy-soft) 0%, var(--navy) 75%);
  }
  .author {
    position: absolute;
    left: 320px;
    top: 1020px;
    color: var(--teal);
    font-weight: 600;
    font-size: 56px;
    line-height: 48px;
    letter-spacing: -1px;
  }
</style>
</head>
<body>
  <main class="cover">
    <svg class="cover__art" viewBox="0 0 848 1200" aria-hidden="true">
      <polygon class="cover__shadow" points="0,0 392,768 848,984 848,1200 0,1200"/>
      <text class="title title__top" x="201" y="330" font-size="262" textLength="586" lengthAdjust="spacingAndGlyphs">LEADER</text>
      <text class="title title__bottom" x="292" y="608" font-size="390" textLength="503" lengthAdjust="spacingAndGlyphs">SHIP</text>
    </svg>

    <p class="subtitle">Fostering Growth and<br>Inspiring Excellence</p>

    <div class="walkers" role="img" aria-label="Illustration: small group of light blue figures walking up the shadowed slope toward a leader at its edge"></div>

    <p class="author">Daniel<br>Hartley</p>
  </main>
</body>
</html>
```